Photovoltaik Anbieter sucht Transporterbeschriftung
Zielgruppe
Kalvberg Planungs- und Betriebs GmbH plant und installiert Photovoltaikanlagen für industrielle Großanlagen. Im Landkreis Lüneburg sind wir der größte Anbieter und bauen und betreuen vornehmlich große Projekte. Unser Anspruch ist es dabei, professionell und perfektionistisch zu arbeiten, um die höchste Qualität gewährleisten zu können. Unsere Zielgruppe sind große industrielle Unternehmen, Besitzer von Freiflächen, Energieversorger und landwirtschaftliche Kunden.
Aufgabenstellung
Design:
...technisch und kühl, professionell, auf Industrie zugeschnitten
...inklusive bestehendem Logo
...Farben aus Logo: gelb, grau
...entweder mit grafischen Elementen oder mit Bildern von technischen Details, Single Line Diagramm, Trafo/Stromspeicher Icon usw.
...Eye-Catcher, hebt sich im besten Fall von lokaler Konkurrenz ab, fällt auf
Bitte nicht das Design von der Website beachten! Diese ist veraltet und wird derzeit bearbeitet

```html
<!DOCTYPE html>
<html lang="de">
<head>
<meta charset="utf-8">
<title>Kalvberg – Transporterbeschriftung Seitenansicht</title>
<link href="https://fonts.googleapis.com/css2?family=Archivo:wght@400;800&display=swap" rel="stylesheet">
<style>
  :root {
    --canvas-bg: #efefef;
    --wrap-white: #ffffff;
    --brand-yellow: #eeba43;
    --brand-grey: #6e6e71;
    --brand-grey-text: #6b6b6e;
    --band-dark: #3a3a3d;
    --band-light: #7a7a7d;
    --glass: #48494c;
    --tyre: #2b2b2d;
    --rim: #b9b9bb;
  }
  html, body {
    margin: 0;
    padding: 0;
    width: 1200px;
    height: 600px;
    overflow: hidden;
    background: var(--canvas-bg);
  }
  .livery {
    position: relative;
    width: 1200px;
    height: 600px;
    font-family: "Archivo", Arial, sans-serif;
  }
  .livery-art {
    position: absolute;
    inset: 0;
  }
  .brand-mark {
    position: absolute;
    left: 540px;
    top: 124px;
    width: 492px;
    height: 138px;
    display: flex;
    align-items: center;
    gap: 22px;
  }
  .brand-square {
    flex: none;
    width: 138px;
    height: 138px;
    background: var(--brand-grey);
  }
  .brand-name {
    font-weight: 800;
    font-size: 58px;
    letter-spacing: 0.5px;
    color: var(--brand-grey-text);
    line-height: 1;
    white-space: nowrap;
  }
  .tagline {
    position: absolute;
    left: 541px;
    top: 268px;
    margin: 0;
    font-weight: 800;
    font-size: 17px;
    line-height: 23px;
    color: var(--brand-grey-text);
  }
  .phone {
    position: absolute;
    left: 168px;
    top: 306px;
    display: flex;
    align-items: center;
    gap: 4px;
    font-weight: 800;
    font-size: 27px;
    line-height: 1;
    color: var(--brand-grey-text);
    letter-spacing: 0.5px;
  }
  .phone-icon {
    width: 19px;
    height: 21px;
  }
  .web-address {
    position: absolute;
    left: 434px;
    width: 400px;
    top: 443px;
    text-align: center;
    font-weight: 400;
    font-size: 19px;
    line-height: 1;
    color: var(--brand-yellow);
    letter-spacing: 0.2px;
  }
</style>
</head>
<body>
<main class="livery">
  <svg class="livery-art" viewBox="0 0 1200 600" width="1200" height="600" aria-hidden="true">
    <defs>
      <clipPath id="body-clip">
        <path d="M42 478 L44 352 Q50 330 70 322 L140 296 L214 282 L335 142 Q360 120 420 104 L700 93 L1120 94 Q1146 98 1150 120 L1158 250 L1160 470 Q1158 482 1148 482 L42 482 Z"/>
      </clipPath>
    </defs>
    <g class="van-body" clip-path="url(#body-clip)">
      <rect x="0" y="80" width="1200" height="420" fill="var(--wrap-white)"/>
      <path class="grey-sweep" d="M1160 228 C 980 318 600 386 260 392 L40 392 L40 500 L1160 500 Z" fill="var(--brand-grey)"/>
      <path class="sweep-divider" d="M1160 228 C 980 318 600 386 260 392" fill="none" stroke="var(--wrap-white)" stroke-width="5"/>
      <path class="yellow-sweep" d="M86 350 C 300 345 560 336 774 318 C 920 302 1040 275 1122 241 C 1040 285 920 330 774 350 C 600 372 330 384 107 388 Z" fill="var(--brand-yellow)"/>
      <rect class="band-dark" x="40" y="392" width="1120" height="40" fill="var(--band-dark)"/>
      <rect class="band-light" x="280" y="432" width="880" height="50" fill="var(--band-light)"/>
      <path class="front-bumper" d="M40 360 Q70 372 90 392 L280 392 L280 482 L40 482 Z" fill="var(--band-dark)"/>
      <rect class="tail-light" x="1122" y="272" width="32" height="112" rx="4" fill="#a8322e"/>
    </g>
    <path class="window" d="M218 290 L335 150 Q350 136 372 134 L448 130 Q456 131 456 140 L452 246 L335 278 Z" fill="var(--glass)"/>
    <g class="wheel">
      <circle cx="199" cy="464" r="68" fill="var(--tyre)"/>
      <circle cx="199" cy="464" r="42" fill="var(--rim)"/>
    </g>
    <g class="wheel">
      <circle cx="976" cy="464" r="68" fill="var(--tyre)"/>
      <circle cx="976" cy="464" r="42" fill="var(--rim)"/>
    </g>
  </svg>

  <div class="brand-mark">
    <div class="brand-square"></div>
    <span class="brand-name">KALVBERG</span>
  </div>

  <p class="tagline">Nie wieder<br>Strompreis-Erhöhung!</p>

  <div class="phone">
    <svg class="phone-icon" viewBox="0 0 20 22" aria-hidden="true">
      <rect x="0" y="0" width="20" height="22" rx="4" fill="var(--brand-grey-text)"/>
      <path d="M6 4 C4 6 4 10 7 14 C10 18 13 19 15 18 L15 15 L12.5 13.5 L11 15 C9.5 14 8 12 7.5 10 L9 9 L8.5 5.5 Z" fill="var(--wrap-white)"/>
    </svg>
    <span>04139 / 5248</span>
  </div>

  <div class="web-address">WWW.KALVBERG-PV.DE</div>
</main>
</body>
</html>
```